Creative/innovative law firm website

A law firm website that immediately looks different from other law firm websites. We like the color scheme (dark background with warm, neutral colors) and simple, organic logos (trees, leaves, etc.) of this website: https://nimbleway.law/

We'll be offering creative/innovative solutions to complex problems faced by state governments, industries, other law firms, and individuals. We're located in Montana (U.S.A.), and the outdoors is a huge part of our lives and identities.

We will need a home page, an "About Us" page with a separate subpage for each attorney (two attorneys), a blog or "Publications" page, a payment portal (which will integrate with Quindle), and a "Services" page.

```html
<!DOCTYPE html>
<html lang="en">
<head>
<meta charset="utf-8">
<title>Halvorsen &amp; Pryce P.C.</title>
<link rel="stylesheet" href="https://fonts.googleapis.com/css2?family=Libre+Baskerville:wght@400;700&family=Poppins:wght@400;500;600&display=swap">
<style>
:root{
  --navy:#1c2136;
  --navy-deep:#171b2d;
  --orange:#d98a22;
  --orange-soft:#e7a54a;
  --grey:#f0f0f0;
  --ink:#2a2a2a;
  --muted:#6b6b6b;
  --white:#ffffff;
  --serif:"Libre Baskerville", Georgia, serif;
  --sans:"Poppins", Arial, sans-serif;
}
*{margin:0;padding:0;box-sizing:border-box}
html,body{width:1200px;height:4298px;overflow:hidden}
body{position:relative;background:var(--white);font-family:var(--sans);color:var(--ink)}
.abs{position:absolute}
.btn{position:absolute;display:flex;align-items:center;justify-content:center;background:var(--orange);color:var(--white);font-family:var(--serif);font-weight:700;font-size:13px;letter-spacing:.3px;text-transform:uppercase}
.heading{font-family:var(--serif);font-weight:700;color:var(--navy);text-transform:uppercase}
.sub{color:var(--orange);font-size:13px}
.para{font-size:11px;line-height:18.5px;color:var(--muted)}

/* top bar */
.topbar{left:0;top:0;width:1200px;height:33px;background:var(--navy)}
.topbar .follow{left:62px;top:9px;font-size:11px;color:var(--white)}
.topbar .social{left:150px;top:9px;font-size:10.5px;color:var(--white);display:flex;gap:12px}
.topbar .free{left:860px;top:9px;font-size:11px;color:var(--white)}
.topbar .phone-ic{left:983px;top:3px;width:27px;height:27px;border-radius:50%;background:var(--orange)}
.topbar .tel{left:1022px;top:8px;font-family:var(--serif);font-size:13px;color:var(--orange)}

/* header */
.header{left:0;top:33px;width:1200px;height:79px;background:var(--white)}
.brand{display:flex;align-items:center;gap:10px}
.brand .dot{width:30px;height:30px;border-radius:50%;background:var(--orange)}
.brand .name{font-family:var(--serif);font-size:20px;line-height:21px;color:var(--navy)}
.header .brand{position:absolute;left:60px;top:14px}
.nav{left:454px;top:33px;display:flex;gap:20px;font-size:11px;color:var(--navy)}
.nav .active{color:var(--orange);position:relative}
.nav .active:after{content:"";position:absolute;left:-6px;right:-6px;bottom:-7px;height:1px;background:var(--orange)}
.header .btn{left:914px;top:20px;width:226px;height:40px;font-size:14px}

/* hero */
.hero{left:0;top:112px;width:1200px;height:606px}
.hero-title{left:0;top:120px;width:1200px;text-align:center;font-family:var(--serif);font-weight:700;font-size:64px;line-height:70px;color:var(--white)}
.hero-title .amp{color:var(--orange)}
.hero-tag{left:0;top:272px;width:1200px;text-align:center;font-size:16px;color:var(--orange)}
.hero .btn{left:487px;top:318px;width:226px;height:40px}

.band-grey{left:0;top:718px;width:1200px;height:534px;background:var(--grey)}

/* about */
.about-kicker{left:656px;top:765px;font-size:12px;color:var(--orange)}
.about-title{left:655px;top:792px;font-size:30px;line-height:40px}
.about-p1{left:656px;top:880px;width:350px}
.about-p2{left:656px;top:951px;width:350px}
.about .btn{left:657px;top:1061px;width:224px;height:39px}

/* features */
.card{position:absolute;top:1183px;width:260px;height:186px;background:var(--white);border:1px solid #e1e1e1;padding:0 17px}
.card.dark{background:var(--navy);border-color:var(--navy)}
.card svg{position:absolute;left:17px;top:22px}
.card h3{position:absolute;left:17px;top:96px;font-family:var(--serif);font-weight:700;font-size:15px;color:var(--navy)}
.card.dark h3{color:var(--white)}
.card p{position:absolute;left:17px;top:122px;width:220px;font-size:10.5px;line-height:18px;color:var(--muted)}
.card.dark p{color:#cfd1d8}

/* why */
.why-title{left:188px;top:1452px;font-size:30px}
.why-sub{left:188px;top:1496px}
.stat{position:absolute;left:189px;width:373px}
.stat .label{position:absolute;left:2px;top:0;font-size:11px;color:var(--ink)}
.stat .val{position:absolute;right:4px;top:0;font-size:11px;font-weight:600;color:var(--ink)}
.stat .track{position:absolute;left:0;top:26px;width:373px;height:5px;background:var(--navy)}
.stat .fill{position:absolute;left:0;top:0;height:5px;background:var(--orange)}
.why-photo{left:676px;top:1435px;width:401px;height:418px}

/* services */
.services{left:0;top:1853px;width:1200px;height:851px;background:var(--navy)}
.svc-kicker{left:0;top:76px;width:1200px;text-align:center;font-size:13px;color:var(--orange)}
.svc-title{left:0;top:102px;width:1200px;text-align:center;font-size:30px;color:var(--white)}
.tile{position:absolute}
.tile-label{position:absolute;left:0;width:100%;top:134px;text-align:center;font-family:var(--serif);font-weight:700;font-size:15px;color:var(--navy)}
.tile-plus{position:absolute;left:183px;top:77px;width:44px;height:44px;border-radius:50%;background:var(--navy)}
.services .btn{left:487px;top:696px;width:226px;height:38px}

.band-grey2{left:0;top:2704px;width:1200px;height:542px;background:var(--grey)}

/* team */
.team-title{left:0;top:2762px;width:1200px;text-align:center;font-size:30px}
.team-sub{left:0;top:2808px;width:1200px;text-align:center}
.member{position:absolute;top:2857px;width:290px;height:311px;background:var(--white)}
.member .photo{position:absolute;left:40px;top:18px;width:210px;height:228px}
.member .tag{position:absolute;left:33px;top:246px;width:225px;height:65px;background:var(--orange);color:var(--white);text-align:center;padding-top:16px}
.member .tag b{display:block;font-family:var(--serif);font-size:15px}
.member .tag span{font-size:12px}

/* blog */
.blog-title{left:0;top:3336px;width:1200px;text-align:center;font-size:30px}
.post{position:absolute;top:3406px;width:285px;height:363px;background:var(--white);box-shadow:0 2px 8px rgba(0,0,0,.08)}
.post .photo{position:absolute;left:0;top:0;width:285px;height:196px}
.post .cat{position:absolute;right:0;top:178px;width:104px;height:33px;background:var(--orange);color:var(--white);font-family:var(--serif);font-weight:700;font-size:14px;display:flex;align-items:center;justify-content:center}
.post .meta{position:absolute;left:18px;top:228px;font-size:10px;color:var(--muted)}
.post h4{position:absolute;left:18px;top:253px;width:250px;font-family:var(--serif);font-weight:700;font-size:14px;line-height:22px;color:var(--navy)}
.post .more{position:absolute;left:18px;top:322px;font-size:10px;color:var(--orange);text-decoration:underline}

/* partners */
.partners{left:0;top:3849px;width:1200px;height:150px;background:var(--grey)}
.partner{position:absolute;top:60px;font-size:27px;color:#6f6f6f;font-family:var(--sans);font-weight:500}

/* footer */
.footer{left:0;top:3999px;width:1200px;height:257px;background:var(--navy)}
.footer .brand{position:absolute;left:75px;top:66px}
.footer .brand .name{color:var(--white);font-size:21px}
.footer .socials{left:121px;top:164px;display:flex;gap:8px}
.footer .socials span{width:35px;height:35px;background:var(--orange);color:var(--navy);font-size:11px;font-weight:600;display:flex;align-items:center;justify-content:center}
.fhead{font-family:var(--serif);font-weight:700;font-size:14px;color:var(--orange);text-transform:uppercase}
.flinks{left:337px;top:86px;list-style:none;font-size:11px;line-height:22.5px;color:var(--white)}
.flinks li:before{content:"\2022";color:var(--orange);margin-right:10px;font-size:9px}
.fnews{left:611px;top:86px;font-size:11px;color:var(--white)}
.finput{left:611px;top:110px;width:251px;height:38px;background:var(--white);font-size:10px;color:#999;padding:12px 13px}
.footer .btn{left:611px;top:163px;width:112px;height:38px}
.fcontact{left:886px;top:84px;width:240px}
.fcontact .row{position:absolute;left:35px;font-size:11px;line-height:18px;color:var(--white)}
.fcontact .ic{position:absolute;left:0;width:20px;height:20px}
.bottom{left:0;top:4256px;width:1200px;height:42px;background:var(--orange);color:var(--white);font-size:11px;text-align:center;padding-top:13px}
</style>
</head>
<body>

<!-- top bar -->
<div class="abs topbar">
  <div class="abs follow">Follow Us On :</div>
  <div class="abs social"><span>Fb</span><span>Ig</span><span>Li</span></div>
  <div class="abs free">Free Consultation :</div>
  <svg class="abs phone-ic" viewBox="0 0 27 27"><circle cx="13.5" cy="13.5" r="13.5" fill="#d98a22"/><path d="M9 8c1 0 2 2.5 2 3s-1 1-1 1.5c.5 1.5 2 3 3.5 3.5.5 0 1-1 1.5-1s3 1 3 2c0 1.5-1.5 2-2.5 2C11 19 8 15 8 10.5 8 9 8.5 8 9 8z" fill="#fff"/></svg>
  <div class="abs tel">+1 123 456 7890</div>
</div>

<!-- header -->
<header class="abs header">
  <div class="brand"><span class="dot"></span><span class="name">Halvorsen &amp;<br>Pryce P.C.</span></div>
  <nav class="abs nav">
    <span class="active">HOME</span><span>ABOUT US</span><span>SERVICES</span><span>PUBLICATION</span><span>PAYMENTS</span><span>CONTACT US</span>
  </nav>
  <div class="btn">Request Consultation</div>
</header>

<!-- hero -->
<section class="abs hero">
  <svg class="abs" style="left:0;top:0" width="1200" height="606" viewBox="0 0 1200 606">
    <defs>
      <linearGradient id="heroShade" x1="0" y1="0" x2="1" y2="1">
        <stop offset="0" stop-color="#3b3129"/>
        <stop offset=".5" stop-color="#2a2524"/>
        <stop offset="1" stop-color="#4a3625"/>
      </linearGradient>
    </defs>
    <rect width="1200" height="606" fill="url(#heroShade)" role="img" aria-label="Photo of a legal team meeting around a table with laptops"/>
    <polygon points="0,514 400,602 1200,492 1200,606 0,606" fill="#f0f0f0"/>
    <polyline points="0,508 400,598 1200,486" fill="none" stroke="#d98a22" stroke-width="4"/>
  </svg>
  <div class="abs hero-title">Halvorsen <span class="amp">&amp;</span><br>Pryce P.C.</div>
  <div class="abs hero-tag">Innovative Solutions To Complex Problems</div>
  <div class="btn">Request Consultation</div>
</section>

<div class="abs band-grey"></div>

<!-- about -->
<section class="about">
  <svg class="abs" style="left:0;top:0" width="1200" height="1120" viewBox="0 0 1200 1120">
    <defs>
      <linearGradient id="aboutShade" x1="0" y1="0" x2="1" y2="1">
        <stop offset="0" stop-color="#5a4a38"/>
        <stop offset=".6" stop-color="#a89a87"/>
        <stop offset="1" stop-color="#d8d2c8"/>
      </linearGradient>
    </defs>
    <polygon points="405,784 587,960 531,1110 297,1110 217,960" fill="url(#aboutShade)" role="img" aria-label="Photo of scales of justice and a hand signing a document"/>
  </svg>
  <div class="abs about-kicker">ABOUT US</div>
  <h2 class="abs heading about-title">Halvorsen &amp;<br>Pryce P.C</h2>
  <p class="abs para about-p1">Lorem Ipsum has been the industry's standard dummythe text ever since the1500s, when an unknown printer took a an galley of type and scrambled specimen book.</p>
  <p class="abs para about-p2">Lorem Ipsum has been the industry's standard dummy text ever since the when an unknown printer took a galley of the type and scrambled it to make a type specimen book. It has survived not only five centuries, but also the leap electronic typesetting, remaining essentially unchanged.</p>
  <div class="btn">Request Consultation</div>
</section>

<!-- features -->
<div class="card dark" style="left:189px">
  <svg width="34" height="48" viewBox="0 0 34 48" fill="none" stroke="#d98a22" stroke-width="2"><rect x="3" y="20" width="28" height="24" rx="2"/><path d="M12 20v-5h10v5M3 30h28"/><circle cx="17" cy="8" r="5"/></svg>
  <h3>Professional Lawyers</h3>
  <p>Lorem Ipsum has been the industry's standard dummythe text.</p>
</div>
<div class="card" style="left:474px">
  <svg width="48" height="48" viewBox="0 0 48 48" fill="none" stroke="#d98a22" stroke-width="2"><path d="M6 4h24l6 6v32H6z"/><path d="M12 14h16M12 20h16M12 26h10"/><circle cx="32" cy="32" r="7"/><path d="M37 37l7 7M29 32l2 2 4-4"/></svg>
  <h3>Document Reviewing</h3>
  <p>Lorem Ipsum has been the industry's standard dummythe text.</p>
</div>
<div class="card" style="left:758px">
  <svg width="48" height="48" viewBox="0 0 48 48" fill="none" stroke="#d98a22" stroke-width="2"><path d="M8 12c3-3 6 3 6 5s-3 2-3 4c2 5 6 9 11 11 2 0 2-3 4-3s8 3 5 6c-3 4-8 4-14 0S6 24 5 18c0-3 1-5 3-6z"/><circle cx="34" cy="14" r="11"/><text x="28" y="18" font-size="10" fill="#d98a22" stroke="none" font-family="Poppins, sans-serif">24</text></svg>
  <h3>24 / Support</h3>
  <p>Lorem Ipsum has been the industry's standard dummythe text.</p>
</div>

<!-- why choose us -->
<h2 class="abs heading why-title">Why Choose Us</h2>
<div class="abs sub why-sub">We Solve Care Professionally</div>
<div class="stat" style="top:1551px"><span class="label">Success Cases</span><span class="val">80%</span><div class="track"><div class="fill" style="width:80%"></div></div></div>
<div class="stat" style="top:1618px"><span class="label">Case Experience</span><span class="val">90%</span><div class="track"><div class="fill" style="width:90%"></div></div></div>
<div class="stat" style="top:1689px"><span class="label">Industries</span><span class="val">60%</span><div class="track"><div class="fill" style="width:64%"></div></div></div>
<div class="abs why-photo" role="img" aria-label="Portrait of a smiling attorney in a dark suit" style="background:radial-gradient(ellipse at 50% 55%, #2a2f45 0 38%, #f6ece0 39% 60%, #ffffff 61%)"></div>

<!-- services -->
<section class="abs services">
  <div class="abs svc-kicker">What We Do</div>
  <h2 class="abs heading svc-title">Services We Provide</h2>
  <div class="tile" role="img" aria-label="Photo of two lawyers reviewing a tablet" style="left:117px;top:173px;width:262px;height:242px;background:linear-gradient(135deg,#8a8f98,#3d3f48)"></div>
  <div class="tile" role="img" aria-label="Photo of a government courthouse facade" style="left:394px;top:173px;width:412px;height:242px;background:linear-gradient(180deg,#d9a052,#c98a34)">
    <svg class="tile-plus" viewBox="0 0 44 44"><circle cx="22" cy="22" r="22" fill="#1c2136"/><path d="M22 13v18M13 22h18" stroke="#fff" stroke-width="1.5"/></svg>
    <div class="tile-label">STATE GOVERNMENTS</div>
  </div>
  <div class="tile" role="img" aria-label="Photo of a judge's gavel beside an open book" style="left:821px;top:173px;width:262px;height:242px;background:linear-gradient(135deg,#e8e3da,#6a5443)"></div>
  <div class="tile" role="img" aria-label="Photo of a handshake in front of international flags" style="left:117px;top:432px;width:479px;height:239px;background:linear-gradient(100deg,#a9543e,#5a6e9a 55%,#2d4c8a)"></div>
  <div class="tile" role="img" aria-label="Photo of a gavel in front of a hard hat" style="left:611px;top:432px;width:472px;height:239px;background:linear-gradient(135deg,#6a5a38,#2a2418)"></div>
  <div class="btn">Request Consultation</div>
  <svg class="abs" style="left:0;top:700px" width="1200" height="151" viewBox="0 0 1200 151">
    <polygon points="0,39 809,151 1200,72 1200,151 0,151" fill="#f0f0f0"/>
    <polyline points="0,33 809,147 1200,66" fill="none" stroke="#d98a22" stroke-width="4"/>
  </svg>
</section>

<div class="abs band-grey2"></div>

<!-- team -->
<h2 class="abs heading team-title">Meet Our Team</h2>
<div class="abs sub team-sub">We Solve Care Professionally</div>
<div class="member" style="left:299px">
  <div class="photo" role="img" aria-label="Portrait of a team member lawyer" style="background:linear-gradient(180deg,#ffffff 30%,#2b2f3d)"></div>
  <div class="tag"><b>MEMBER NAME</b><span>Lawyer</span></div>
</div>
<div class="member" style="left:611px">
  <div class="photo" role="img" aria-label="Portrait of a team member lawyer" style="background:linear-gradient(180deg,#ffffff 30%,#23273a)"></div>
  <div class="tag"><b>MEMBER NAME</b><span>Lawyer</span></div>
</div>

<!-- blog -->
<h2 class="abs heading blog-title">Latest Blog</h2>
<article class="post" style="left:154px">
  <div class="photo" role="img" aria-label="Photo of a lawyer speaking in a courtroom" style="background:linear-gradient(180deg,#b08a62,#4a3322)"></div>
  <div class="cat">Lawyers</div>
  <div class="meta">&bull;&nbsp;&nbsp;7 Dec 2021 &nbsp;&nbsp;&nbsp;&bull;&nbsp;&nbsp;by Halvorsen</div>
  <h4>Lorem Ipsum Has Bee Industry's Standard dummythe</h4>
  <div class="more">READ MORE</div>
</article>
<article class="post" style="left:457px">
  <div class="photo" role="img" aria-label="Photo of lawyers meeting with a client in an office" style="background:linear-gradient(180deg,#9a948c,#35353d)"></div>
  <div class="cat">Lawyers</div>
  <div class="meta">&bull;&nbsp;&nbsp;7 Dec 2021 &nbsp;&nbsp;&nbsp;&bull;&nbsp;&nbsp;by Halvorsen</div>
  <h4>Lorem Ipsum Has Bee Industry's Standard dummythe</h4>
  <div class="more">READ MORE</div>
</article>
<article class="post" style="left:761px">
  <div class="photo" role="img" aria-label="Photo of hands reviewing contract papers" style="background:linear-gradient(180deg,#e9e4dc,#7a6a58)"></div>
  <div class="cat">Lawyers</div>
  <div class="meta">&bull;&nbsp;&nbsp;7 Dec 2021 &nbsp;&nbsp;&nbsp;&bull;&nbsp;&nbsp;by Halvorsen</div>
  <h4>Lorem Ipsum Has Bee Industry's Standard dummythe</h4>
  <div class="more">READ MORE</div>
</article>

<!-- partners -->
<section class="abs partners">
  <span class="partner" style="left:124px">Quarvel</span>
  <span class="partner" style="left:296px">Tessmark</span>
  <span class="partner" style="left:478px">ledgerwise</span>
  <span class="partner" style="left:752px">Brindle Suite</span>
  <span class="partner" style="left:935px">Corvane</span>
</section>

<!-- footer -->
<footer class="abs footer">
  <div class="brand"><span class="dot"></span><span class="name">Halvorsen &amp;<br>Pryce P.C.</span></div>
  <div class="abs socials"><span>Fb</span><span>Ig</span><span>Li</span></div>

  <div class="abs fhead" style="left:336px;top:45px">Sitemap</div>
  <ul class="abs flinks"><li>Home</li><li>About Us</li><li>Services</li><li>Publication</li><li>Payments</li></ul>

  <div class="abs fhead" style="left:611px;top:45px">Newsletter Signup !</div>
  <div class="abs fnews">Stay upto date with our publication !</div>
  <div class="abs finput">Enter Email *</div>
  <div class="btn">Subscribe</div>

  <div class="abs fhead" style="left:886px;top:45px">Contact Us</div>
  <div class="abs fcontact">
    <svg class="ic" style="top:0" viewBox="0 0 20 20"><path d="M10 1a6 6 0 0 0-6 6c0 5 6 12 6 12s6-7 6-12a6 6 0 0 0-6-6z" fill="none" stroke="#d98a22" stroke-width="2"/><circle cx="10" cy="7" r="2" fill="#d98a22"/></svg>
    <div class="row" style="top:0"><span style="color:#d98a22">Halvorsen &amp; Pryce P.C.</span><br>101 - lorem ipsum simple text<br>print type setting industry.</div>
    <svg class="ic" style="top:74px" viewBox="0 0 20 20"><path d="M4 2c2 0 3 4 3 5s-2 1-2 2c1 3 3 5 6 6 1 0 1-2 2-2s5 1 5 3c0 2-2 3-4 3C7 19 1 13 1 6c0-2 1-4 3-4z" fill="#d98a22"/></svg>
    <div class="row" style="top:74px;font-size:13px">123 456 7890</div>
    <svg class="ic" style="top:105px" viewBox="0 0 20 20"><rect x="1" y="4" width="18" height="12" fill="#d98a22"/><path d="M1 4l9 7 9-7" fill="none" stroke="#1c2136" stroke-width="1.5"/></svg>
    <div class="row" style="top:105px">info@halvorsenpryce.com</div>
  </div>
</footer>
<div class="abs bottom">&copy;Halvorsen &amp; Pryce P.C. - 2021 All rights reserved.</div>

</body>
</html>
```